Crestline Lending Group Business Cards

We are looking to revamp the current business cards each of our locations uses. We are a lending company that specializes in personal loans, title loans, and tax services. We have locations in New Mexico, Texas, and Oklahoma.

We would like a cleaner, sleeker look while still highlighting what we offer. Title Loans, Personal Loans & Tax Services. We also want to include our referral fee somewhere on the card. We would like to see an English option as well as a Spanish option for the cards.

PLEASE NOTE: Some business cards do not include the employee's name but just the store's location, while others will include both.

These are double-sided business cards, and we would like to see proof if possible. I have included proofs of our current business cards for you to review below, as well as our company logo. Feel free to get creative with the logo, etc! Colors should match the logo; however, you do not need to use all of our logo colors if you don't want to.

```html
<!DOCTYPE html>
<html lang="en">
<head>
<meta charset="utf-8">
<title>Crestline Lending Group – Business Card</title>
<link href="https://fonts.googleapis.com/css2?family=Libre+Baskerville:wght@400;700&family=Poppins:wght@400;500;600;700&display=swap" rel="stylesheet">
<style>
  :root {
    --green: #0d5130;
    --red: #c21f2a;
    --white: #ffffff;
    --ink: #1c1c1c;
    --backdrop: #c9c9c9;
  }
  * { box-sizing: border-box; margin: 0; padding: 0; }
  html, body { width: 1200px; height: 800px; overflow: hidden; }
  body {
    background: var(--backdrop);
    font-family: "Poppins", sans-serif;
    display: flex;
    align-items: center;
    justify-content: center;
    gap: 40px;
  }
  .card {
    position: relative;
    width: 540px;
    height: 309px;
    overflow: hidden;
    border-bottom: 2px solid var(--red);
  }

  /* Front */
  .card--front { background: var(--white); }
  .card__band { position: absolute; inset: 0; width: 100%; height: 100%; }
  .brand {
    position: absolute;
    top: 34px;
    right: 30px;
    text-align: right;
  }
  .brand__name {
    font-family: "Libre Baskerville", serif;
    font-weight: 700;
    font-size: 22px;
    line-height: 1.15;
    color: var(--green);
  }
  .brand__url {
    margin-top: 6px;
    font-size: 12px;
    font-weight: 500;
    color: var(--red);
    letter-spacing: 0.3px;
  }
  .contact {
    position: absolute;
    left: 30px;
    top: 118px;
  }
  .contact__name {
    font-family: "Libre Baskerville", serif;
    font-weight: 700;
    font-size: 22px;
    color: var(--green);
    line-height: 1.1;
  }
  .contact__role {
    font-size: 13px;
    color: var(--red);
    margin-bottom: 8px;
  }
  .contact__line {
    display: flex;
    align-items: center;
    gap: 7px;
    font-size: 12.5px;
    color: var(--ink);
    line-height: 1.5;
  }
  .contact__icon { width: 12px; height: 12px; flex: none; }
  .contact__address {
    margin-top: 10px;
    font-size: 12.5px;
    color: var(--ink);
    line-height: 1.45;
  }
  .services {
    position: absolute;
    right: 24px;
    bottom: 26px;
    font-size: 12.5px;
    color: var(--white);
    letter-spacing: 0.3px;
  }
  .services__dot { color: var(--red); margin: 0 6px; }

  /* Back */
  .card--back {
    background: var(--green);
    display: flex;
    flex-direction: column;
    align-items: center;
    justify-content: center;
    text-align: center;
  }
  .back__brand {
    font-family: "Libre Baskerville", serif;
    font-weight: 700;
    font-size: 30px;
    color: var(--white);
    line-height: 1.2;
    margin-bottom: 30px;
  }
  .referral__lead {
    font-size: 26px;
    font-weight: 600;
    color: var(--white);
    line-height: 1.1;
  }
  .referral__offer {
    font-size: 46px;
    font-weight: 700;
    color: var(--red);
    line-height: 1.1;
  }
</style>
</head>
<body>

  <section class="card card--front" aria-label="Business card front">
    <svg class="card__band" viewBox="0 0 540 309" preserveAspectRatio="none" aria-hidden="true">
      <path d="M0,309 C170,300 380,190 540,140 L540,148 C380,202 180,304 0,309 Z" fill="var(--red)"/>
      <path d="M0,309 C180,306 390,210 540,160 L540,309 Z" fill="var(--green)"/>
    </svg>

    <div class="brand">
      <div class="brand__name">Crestline<br>Lending Group</div>
      <div class="brand__url">www.crestlinelending.com</div>
    </div>

    <div class="contact">
      <div class="contact__name">Jane Doe</div>
      <div class="contact__role">Branch Manager</div>
      <div class="contact__line">
        <svg class="contact__icon" viewBox="0 0 24 24" aria-hidden="true"><path fill="var(--green)" d="M6.6 10.8a15.1 15.1 0 0 0 6.6 6.6l2.2-2.2a1 1 0 0 1 1-.25 11.4 11.4 0 0 0 3.6.57 1 1 0 0 1 1 1V20a1 1 0 0 1-1 1A17 17 0 0 1 3 4a1 1 0 0 1 1-1h3.5a1 1 0 0 1 1 1c0 1.250.2 2.450.57 3.57a1 1 0 0 1-.25 1z"/></svg>
        <span>(575) 555-0184</span>
      </div>
      <div class="contact__line">
        <svg class="contact__icon" viewBox="0 0 24 24" aria-hidden="true"><path fill="var(--green)" d="M2 5h20v14H2z"/><path d="M2 5l10 8 10-8" fill="none" stroke="var(--white)" stroke-width="2"/></svg>
        <span>hello@crestlinelending.com</span>
      </div>
      <div class="contact__address">480 Ridge Road, Suite C<br>Millbrook, Texas 75012</div>
    </div>

    <div class="services">Title Loans<span class="services__dot">•</span>Personal Loans<span class="services__dot">•</span>Tax Services</div>
  </section>

  <section class="card card--back" aria-label="Business card back">
    <div class="back__brand">Crestline Lending Group</div>
    <div class="referral__lead">Refer a Friend</div>
    <div class="referral__offer">Get Upto $100</div>
  </section>

</body>
</html>
```